Morvela Aesthetic Doctor

I require an elegant, luxurious looking business card for my aesthetic business. I am a doctor and that will set me aside from competitors. I am planning to provide home and spa based treatments to clients with high expectations. I have attached my logo.

```html
<!DOCTYPE html>
<html lang="en">
<head>
<meta charset="utf-8">
<title>Morvela Aesthetic Doctor – Business Card</title>
<link rel="stylesheet" href="https://fonts.googleapis.com/css2?family=Marcellus&family=Roboto:ital,wght@0,300;0,400;1,400&family=Raleway:wght@500&display=swap">
<style>
  :root {
    --backdrop: #c8c8c8;
    --blue-light: #4ea8dc;
    --blue-deep: #0a64a4;
    --band-grey: #9aa1a8;
    --silver-top: #f4f4f4;
    --silver-bottom: #dcdcdc;
    --ink: #2c2c2c;
    --accent: #3a9fd6;
    --pill: #4aa0d2;
    --white: #ffffff;
  }
  * { margin: 0; padding: 0; box-sizing: border-box; }
  html, body { width: 1200px; height: 576px; overflow: hidden; }
  body { background: var(--backdrop); position: relative; font-family: "Roboto", sans-serif; }

  .card {
    position: absolute; top: 138px; width: 484px; height: 294px;
    border-radius: 12px; overflow: hidden;
    box-shadow: 0 3px 6px rgba(0,0,0,0.25);
  }

  /* Front */
  .card-front {
    left: 82px;
    background: linear-gradient(160deg, var(--blue-light) 0%, #2a86c4 45%, var(--blue-deep) 100%);
    color: var(--white);
  }
  .brand-mark {
    position: absolute; left: 50px; top: 52px; width: 96px; height: 96px;
    border: 2px solid rgba(255,255,255,0.85); border-radius: 50%;
  }
  .brand-name {
    position: absolute; left: 162px; top: 58px;
    font-family: "Marcellus", serif; font-weight: 400; color: var(--white);
    line-height: 1;
  }
  .brand-name .name-main { display: block; font-size: 58px; letter-spacing: 1px; }
  .brand-name .name-sub { display: block; font-size: 25px; letter-spacing: 1px; margin-top: 4px; }
  .services {
    position: absolute; left: 0; right: 0; top: 196px;
    text-align: center; font-size: 13px; font-weight: 300; line-height: 18px;
    color: rgba(255,255,255,0.92);
  }
  .services .sep { margin: 0 8px; }
  .treatment-band {
    position: absolute; left: 0; right: 0; top: 245px; height: 25px;
    background: var(--band-grey);
    font-family: "Raleway", sans-serif; font-weight: 500; font-size: 12.5px;
    letter-spacing: 0.8px; line-height: 25px; text-align: center;
    color: var(--white);
  }

  /* Back */
  .card-back {
    left: 602px; width: 481px; height: 292px;
    background: linear-gradient(180deg, var(--silver-top) 0%, var(--silver-bottom) 100%);
    color: var(--ink);
  }
  .decor-silhouette {
    position: absolute; right: 0; top: 0; width: 200px; height: 262px;
    background: radial-gradient(ellipse at 60% 45%, rgba(170,170,170,0.35) 0%, rgba(190,190,190,0.15) 55%, rgba(220,220,220,0) 80%);
  }
  .doctor-name {
    position: absolute; left: 27px; top: 44px;
    font-size: 24px; font-weight: 300; color: var(--ink);
  }
  .credentials {
    position: absolute; left: 27px; top: 72px;
    font-size: 10.5px; font-style: italic; color: var(--accent);
  }
  .qualification {
    position: absolute; left: 27px; top: 85px;
    font-size: 14px; color: var(--accent);
  }
  .contact-list {
    position: absolute; left: 27px; top: 187px; list-style: none;
    font-size: 13px; line-height: 18px; color: var(--ink);
  }
  .contact-list li { display: flex; align-items: center; gap: 8px; }
  .contact-list svg { width: 11px; height: 11px; fill: var(--accent); flex: none; }
  .follow {
    position: absolute; left: 27px; top: 246px;
    display: flex; align-items: center; gap: 6px; font-size: 13px;
  }
  .social-dot { width: 13px; height: 13px; border-radius: 50%; background: var(--accent); }
  .service-pill {
    position: absolute; left: 170px; right: 0; top: 243px; height: 25px;
    background: var(--pill); border-radius: 13px 0 0 13px;
    color: var(--white); font-size: 14px; line-height: 25px; text-align: center;
  }
</style>
</head>
<body>

<section class="card card-front">
  <div class="brand-mark"></div>
  <h1 class="brand-name">
    <span class="name-main">MORVELA</span>
    <span class="name-sub">AESTHETIC DOCTOR</span>
  </h1>
  <p class="services">
    Dermal Injectables<span class="sep">|</span>Plasma Facials<span class="sep">|</span>Microneedling<br>
    Skin Boosters<span class="sep">|</span>Excessive Sweating
  </p>
  <div class="treatment-band">HOME AND SPA BASED TREATMENTS</div>
</section>

<section class="card card-back">
  <div class="decor-silhouette" role="img" aria-label="Faint decorative profile silhouette with flowing hair"></div>
  <h2 class="doctor-name">Dr Elsa Marwick</h2>
  <p class="credentials">MRCPCH MD</p>
  <p class="qualification">Australasian Diploma of Aesthetic Medicine</p>
  <ul class="contact-list">
    <li><svg viewBox="0 0 12 12"><path d="M2.4 0.6 L4.4 0.6 L5 3.4 L3.7 4.5 Q4.8 6.9 7.4 8.3 L8.5 7 L11.4 7.6 L11.4 9.6 Q11.4 11.4 9.6 11.4 Q0.6 10.6 0.6 2.4 Q0.6 0.6 2.4 0.6 Z"/></svg>0800 555 019</li>
    <li><svg viewBox="0 0 12 12"><path d="M0.5 2 H11.5 V10 H0.5 Z M1.2 2.6 L6 6.4 L10.8 2.6 Z" fill-rule="evenodd"/></svg>elsa@morvela.co.nz</li>
    <li><svg viewBox="0 0 12 12"><path d="M6 0.5 A5.5 5.5 0 1 0 6 11.5 A5.5 5.5 0 1 0 6 0.5 Z M6 1.6 A4.4 4.4 0 1 1 6 10.4 A4.4 4.4 0 1 1 6 1.6 Z M1 5.5 H11 V6.5 H1 Z M5.5 1 H6.5 V11 H5.5 Z" fill-rule="evenodd"/></svg>www.morvela.co.nz</li>
  </ul>
  <div class="follow">Follow us on: <span class="social-dot"></span><span class="social-dot"></span></div>
  <div class="service-pill">Home &amp; Spa Based Treatments</div>
</section>

</body>
</html>
```